Vexor Ridge website

i'm looking for a promotional website for my business.
we provide Rope Access, Work at Height & Difficult Access services.
we treat water leak into buildings, external renovation of buildings, windows cleaning, confined spaces services and practically jobs in which the access is difficult.
here are examples of web site i like :
http://www.pixelbarnwebs.example/site-themes/51827.html
http://www.pixelbarnwebs.example/page-templates/62914.html

Target Market(s)

private people, commercial household chiefs, maintenance managers

Industry/Entity Type

Business

Requirements
Must have
• - mobile friendly
- chatterbay redirection
- 5 tabs
- one more customizable page - so i can add a photo and a description of the service corresponding (for now i offer 7 different services)
- contact us on each page with no redirection
- we are offering 7 different services
the website will be published in Israel which means right to left or centered for english option in the future. (logo on left hand corner)

- no flash
- should be future customisable - for future
Nice to have
• - a space for a slogan
- non scrollable
- photos on the landing page + redirection to gallery (photos and short films)
- 3 dynamic banners with short description of the theme of each, clicking on the banner after it opened will redirect to it's corresponding page.

```html
<!DOCTYPE html>
<html lang="en">
<head>
<meta charset="utf-8">
<title>Vexor Ridge – Rope Access, Work at Height &amp; Difficult Access</title>
<link rel="stylesheet" href="https://fonts.googleapis.com/css2?family=Yanone+Kaffeesatz:wght@300;400&family=Indie+Flower&family=Arimo:wght@400;700&display=swap">
<style>
:root{
  --red:#ff1a0d;
  --red-dark:#7a0d08;
  --red-logo:#f5241c;
  --amber:#f6a800;
  --orange:#ff9000;
  --ink:#111;
  --text:#333;
  --line:#c9c9c9;
  --white:#fff;
  --page-top:#e4e4e4;
  --page-mid:#f3f3f3;
}
*{box-sizing:border-box;margin:0;padding:0}
html,body{width:955px;height:1200px;overflow:hidden}
body{position:relative;font-family:"Arimo",Arial,sans-serif;color:var(--text);
  background:linear-gradient(180deg,var(--page-top) 0,var(--page-mid) 260px,#f7f7f7 600px,#fff 1000px)}

/* header */
.call-badge{position:absolute;display:flex;align-items:center;gap:5px;height:20px;padding:0 14px 0 10px;white-space:nowrap;
  font-size:11px;color:var(--white);background:var(--ink);border-radius:10px 0 0 10px;
  clip-path:polygon(0 0,88% 0,100% 50%,88% 100%,0 100%)}
.call-badge.amber{background:var(--amber);color:#3a2a00}
.phone-number{position:absolute;font-family:"Indie Flower",cursive;font-size:29px;line-height:36px;color:var(--ink);white-space:nowrap}
.phone-number.light{color:var(--white)}

.logo{position:absolute;left:96px;top:25px;width:127px;height:127px;border-radius:50%;background:var(--red-logo);
  box-shadow:0 2px 6px rgba(0,0,0,.25);display:flex;align-items:center;justify-content:center;z-index:3}
.logo::before{content:"";position:absolute;inset:7px;border-radius:50%;border:1px dashed rgba(255,255,255,.55)}
.logo-name{font-family:"Yanone Kaffeesatz",sans-serif;font-weight:400;font-size:30px;line-height:.95;color:var(--ink);text-align:center}

.main-nav{position:absolute;left:102px;top:67px;width:748px;height:47px;background:var(--red);z-index:2}
.nav-links{position:absolute;right:152px;top:0;height:47px;display:flex}
.nav-links a{font-family:"Yanone Kaffeesatz",sans-serif;font-weight:300;font-size:21px;color:var(--white);text-decoration:none;
  display:flex;align-items:center;padding:0 15px;white-space:nowrap}
.nav-links a.active{background:var(--red-dark)}
.search{position:absolute;left:610px;top:13px;width:126px;height:21px;background:rgba(255,255,255,.18);
  font-size:11px;color:rgba(255,255,255,.7);padding:4px 8px}
.search svg{position:absolute;right:6px;top:6px}

/* hero */
.hero{position:absolute;left:102px;top:114px;width:748px;height:388px;
  background:linear-gradient(180deg,#2b2a28 0%,#56524c 30%,#3f5e63 62%,#5e8e8e 85%,#2f4b4c 100%)}
.hero-shade{position:absolute;inset:0;background:linear-gradient(180deg,rgba(0,0,0,0) 35%,rgba(0,0,0,.25) 55%,rgba(0,0,0,0) 75%)}
.hero-title{position:absolute;left:0;right:0;top:152px;text-align:center;font-family:"Yanone Kaffeesatz",sans-serif;font-weight:400;
  font-size:36px;line-height:44px;color:var(--white);white-space:nowrap}
.hero-text{position:absolute;left:0;right:0;top:200px;text-align:center;font-size:15.5px;line-height:24px;color:#f0f0f0;letter-spacing:-.2px}
.hero-text span.line{display:block;white-space:nowrap}
.quote-btn{display:inline-block;vertical-align:middle;margin-left:6px;height:20px;padding:3px 18px 0 12px;font-size:11px;color:#2a1d00;letter-spacing:0;
  background:var(--amber);border-radius:10px 0 0 10px;clip-path:polygon(0 0,90% 0,100% 50%,90% 100%,0 100%);line-height:14px}
.slide-thumbs{position:absolute;top:299px;left:312px;display:flex;gap:3px}
.slide-thumb{width:41px;height:41px;border-radius:50%;border:2px solid var(--white)}
.slide-thumb.current{border-color:var(--amber)}
.slide-arrow{position:absolute;top:255px;width:28px;height:42px;background:var(--ink);display:flex;align-items:center;justify-content:center}
.slide-arrow.prev{left:74px;border-radius:21px 0 0 21px}
.slide-arrow.next{left:850px;border-radius:0 21px 21px 0}

.projects-tab{position:absolute;left:723px;top:502px;width:127px;height:27px;background:var(--red);color:var(--white);font-size:11px;
  display:flex;align-items:center;padding-left:22px;gap:8px;clip-path:polygon(0 0,100% 0,100% 100%,10% 100%)}

/* services */
.section-title{position:absolute;left:0;width:955px;top:518px;text-align:center;font-family:"Yanone Kaffeesatz",sans-serif;font-weight:400;
  font-size:40px;line-height:46px;color:var(--red)}
.title-rule{position:absolute;top:548px;height:3px;width:42px;background:var(--red)}
.dash{position:absolute;left:105px;width:744px;border-top:1px dashed var(--line)}

.service{position:absolute;top:618px;width:196px;text-align:center}
.service-tile{width:116px;height:116px;margin:27px auto 0;border-radius:10px;transform:rotate(45deg);box-shadow:0 6px 10px rgba(0,0,0,.12)}
.service-shadow{width:110px;height:8px;margin:30px auto 0;border-radius:50%;background:radial-gradient(rgba(0,0,0,.18),rgba(0,0,0,0) 70%)}
.service-name{font-family:"Yanone Kaffeesatz",sans-serif;font-weight:400;font-size:23px;line-height:28px;color:var(--ink);margin-top:6px}
.service-text{font-size:12px;line-height:15px;color:var(--text);margin-top:5px}
.more-btn{display:inline-block;margin-top:10px;padding:1px 6px;background:var(--orange);color:var(--white);font-size:11px}

/* clients */
.clients{position:absolute;left:102px;top:942px;width:748px;height:77px;background:var(--white)}
.clients-tag{position:absolute;left:14px;top:25px;width:87px;height:24px;background:#dedede;font-size:11px;color:var(--ink);
  display:flex;align-items:center;padding-left:10px;clip-path:polygon(0 0,88% 0,100% 50%,88% 100%,0 100%)}
.client{position:absolute;top:26px;font-family:"Arimo",sans-serif;font-weight:700;font-size:18px;color:#b5b5b5;display:flex;align-items:center;gap:5px}
.client i{display:inline-block;width:14px;height:14px;border-radius:50%;background:#c4c4c4}

/* footer */
.site-footer{position:absolute;left:0;top:1056px;width:955px;height:144px;background:var(--red)}
.footer-links{position:absolute;left:102px;top:58px;font-size:9.5px;color:var(--white);white-space:nowrap}
.footer-links span{margin:0 4px}
.copyright{position:absolute;left:102px;top:75px;font-size:9.5px;color:var(--white);white-space:nowrap}
.social{position:absolute;top:70px;left:432px;display:flex;gap:9px}
.social a{color:var(--white);font-size:10px;text-decoration:none;white-space:nowrap}
</style>
</head>
<body>

<header>
  <div class="call-badge" style="left:562px;top:25px">
    <svg width="10" height="10" viewBox="0 0 10 10"><path d="M2 0.5 L3.6 0.5 L4.2 2.8 L3 3.6 Q4 5.8 6.4 7 L7.2 5.8 L9.5 6.4 L9.5 8 Q9.5 9.5 8 9.5 Q1 8.5 0.5 2 Q0.5 0.5 2 0.5Z" fill="#fff"/></svg>
    Call 24x7
  </div>
  <div class="phone-number" style="left:644px;top:16px">(0135) 724 6081</div>

  <div class="logo"><span class="logo-name">Vexor<br>Ridge</span></div>

  <nav class="main-nav">
    <div class="nav-links">
      <a href="#">Home</a>
      <a href="#">About Us</a>
      <a href="#" class="active">Services</a>
      <a href="#">Projects</a>
      <a href="#">Contact Us</a>
    </div>
    <div class="search">Search
      <svg width="9" height="9" viewBox="0 0 9 9"><circle cx="3.6" cy="3.6" r="2.6" fill="none" stroke="#fff" stroke-width="1.2"/><path d="M5.5 5.5 L8.5 8.5" stroke="#fff" stroke-width="1.4"/></svg>
    </div>
  </nav>
</header>

<section class="hero" role="img" aria-label="Photo of a rope access technician working among pipes at height">
  <div class="hero-shade"></div>
  <h1 class="hero-title">Rope Access Work at Height &amp; Difficult Access Services</h1>
  <p class="hero-text"><span class="line">Lorem ipsum dolor sit amet, consectetur adipisicing elit, sed do eiusmod tempor incididunt ut</span><span class="line">labore et dolore magna aliqua. Ut enim ad minim veniam <span class="quote-btn">Request a Quote</span></span></p>
  <div class="slide-thumbs">
    <div class="slide-thumb current" role="img" aria-label="Rope access slide thumbnail" style="background:#3d4a48"></div>
    <div class="slide-thumb" role="img" aria-label="Glass facade slide thumbnail" style="background:#7f9dbd"></div>
    <div class="slide-thumb" role="img" aria-label="Rooftop work slide thumbnail" style="background:#8f6e57"></div>
  </div>
</section>
<div class="slide-arrow prev"><svg width="9" height="6"><path d="M0 3 L9 0 L9 6Z" fill="#fff"/></svg></div>
<div class="slide-arrow next"><svg width="9" height="6"><path d="M9 3 L0 0 L0 6Z" fill="#fff"/></svg></div>

<div class="projects-tab">See Our Projects <svg width="11" height="6"><path d="M0 6 L11 3 L3 0 L5 3Z" fill="#fff"/></svg></div>

<main>
  <div class="title-rule" style="left:304px;clip-path:polygon(0 40%,100% 0,100% 100%)"></div>
  <h2 class="section-title">Vexor Ridge Services</h2>
  <div class="title-rule" style="left:608px;clip-path:polygon(0 0,100% 40%,0 100%)"></div>
  <div class="dash" style="top:594px"></div>

  <article class="service" style="left:86px">
    <div class="service-tile" role="img" aria-label="Photo of a glass building facade" style="background:linear-gradient(135deg,#2e4f86,#7aa6db 55%,#24385c)"></div>
    <div class="service-shadow"></div>
    <h3 class="service-name">Difficult Access</h3>
    <p class="service-text">Lorem ipsum dolor amet lorem sit adipisicing elit eiusmod...</p>
    <span class="more-btn">MORE</span>
  </article>
  <article class="service" style="left:282px">
    <div class="service-tile" role="img" aria-label="Photo of a tall tensile canopy mast against the sky" style="background:linear-gradient(135deg,#d9cdc4,#f1ebe4 50%,#8b8a84);border:3px solid #fff"></div>
    <div class="service-shadow"></div>
    <h3 class="service-name">Work at Height</h3>
    <p class="service-text">Lorem ipsum dolor amet lorem sit adipisicing elit eiusmod...</p>
    <span class="more-btn">MORE</span>
  </article>
  <article class="service" style="left:478px">
    <div class="service-tile" role="img" aria-label="Photo of a rope access worker among industrial pipes" style="background:linear-gradient(135deg,#3a3734,#566a66 55%,#4f8385)"></div>
    <div class="service-shadow"></div>
    <h3 class="service-name">Rope Access</h3>
    <p class="service-text">Lorem ipsum dolor amet lorem sit adipisicing elit eiusmod...</p>
    <span class="more-btn">MORE</span>
  </article>
  <article class="service" style="left:670px">
    <div class="service-tile" role="img" aria-label="Photo of a technician in climbing harness cleaning windows" style="background:linear-gradient(135deg,#cfd3d6,#3b3b3b 55%,#d6dadc)"></div>
    <div class="service-shadow"></div>
    <h3 class="service-name">Windows Cleaning</h3>
    <p class="service-text">Lorem ipsum dolor amet lorem sit adipisicing elit eiusmod...</p>
    <span class="more-btn">MORE</span>
  </article>

  <div class="dash" style="top:937px"></div>
  <section class="clients">
    <div class="clients-tag">OUR CLIENTS</div>
    <span class="client" style="left:162px"><i></i>Hostmere</span>
    <span class="client" style="left:292px">Brandol</span>
    <span class="client" style="left:408px">Datavane</span>
    <span class="client" style="left:521px"><i></i>Loopwire</span>
    <span class="client" style="left:638px">Chalkit</span>
  </section>
  <div class="dash" style="top:1021px"></div>
</main>

<footer class="site-footer">
  <div class="footer-links">Home<span>|</span>About us<span>|</span>Services<span>|</span>Projects<span>|</span>Contact us<span>|</span>Privacy Policy</div>
  <div class="copyright">All Right Reserved Copyright © 2013 - Vexor Ridge</div>
  <div class="social">
    <a href="#">chatterbay</a>
    <a href="#">Chirpnest</a>
    <a href="#">Linkhall</a>
  </div>
  <div class="call-badge amber" style="left:588px;top:66px">
    <svg width="10" height="10" viewBox="0 0 10 10"><path d="M2 0.5 L3.6 0.5 L4.2 2.8 L3 3.6 Q4 5.8 6.4 7 L7.2 5.8 L9.5 6.4 L9.5 8 Q9.5 9.5 8 9.5 Q1 8.5 0.5 2 Q0.5 0.5 2 0.5Z" fill="#3a2a00"/></svg>
    Call 24x7
  </div>
  <div class="phone-number light" style="left:670px;top:58px">(0135) 724 6081</div>
</footer>

</body>
</html>
```